Cleaning Company needs a new business card design

Hi, We are looking for new business card designs to update with our latest logo and company information.
We would like to see designs using the colours:
Royal Blue #4169E1 - this is our company colour so this has to be in there. Please feel free to experiment with other colours.
Must include:
Front of business card:
Logo
Back of the business card:
0800 529 6081
07438 915 702
Email: info@pkrtidyhomes.co.uk
Web: www.pkrtidyhomes.co.uk
Services:
End of Tenancy
Carpet & Upholstery
Regular & One Off
all work fully insured.
The front of the business card with the logo can be made to look raised print. The blue man to be a shiny finish.
The business card needs to be presented in a matt finish
The business must be in the following styles:
Standard Square with rounded corners.
Thank you to all that take part in this.
Target Market(s)
Men and Women of different ages in the UK.
Industry/Entity Type
House Cleaning
Contact Information for Business Card
Front of business card:
Logo
0800 529 6081
07438 915 702
Email: pkrtidy@mailbox-demo.co.uk
Services:
End of Tenancy
Carpet & Upholstery
Regular & One Off
all work fully insured.

```html
<!DOCTYPE html>
<html lang="en">
<head>
<meta charset="utf-8">
<title>PKR Tidy Homes – Business Card</title>
<link rel="stylesheet" href="https://fonts.googleapis.com/css2?family=Open+Sans:wght@400;600;700;800&display=swap">
<style>
  :root {
    --page-bg: #e6e7ea;
    --card-white: #ffffff;
    --royal: #2d47a5;
    --royal-text: #2a44a8;
    --sky: #29a3df;
    --logo-pale: #c7d1ea;
    --white: #ffffff;
  }
  * { box-sizing: border-box; margin: 0; padding: 0; }
  html, body {
    width: 1200px; height: 900px; overflow: hidden;
    background: var(--page-bg);
    font-family: "Open Sans", Arial, sans-serif;
  }
  .canvas {
    position: relative; width: 1200px; height: 900px;
    display: flex; align-items: center; justify-content: center; gap: 70px;
  }
  .card {
    position: relative; width: 470px; height: 470px;
    border-radius: 34px; overflow: hidden;
    background: var(--card-white);
    box-shadow: 0 12px 30px rgba(0,0,0,0.18);
  }

  /* Front */
  .card-front { display: flex; flex-direction: column; align-items: center; }
  .brand {
    margin-top: 120px;
    display: flex; align-items: center; gap: 16px;
  }
  .brand-mark {
    width: 44px; height: 44px; border-radius: 50%;
    background: var(--logo-pale);
  }
  .brand-name {
    font-weight: 700; font-size: 40px; line-height: 1.1;
    color: var(--logo-pale); text-align: left;
  }
  .services {
    margin-top: 70px; text-align: center;
    color: var(--royal-text); font-weight: 700;
    font-size: 19px; line-height: 1.3;
  }

  /* Back */
  .card-back .top {
    position: absolute; left: 0; top: 0; width: 100%; height: 215px;
    display: flex; align-items: center; justify-content: center; gap: 14px;
  }
  .back-mark { width: 40px; height: 40px; border-radius: 50%; background: var(--sky); }
  .back-name { font-weight: 700; font-size: 30px; color: var(--sky); }
  .card-back .stripe {
    position: absolute; left: 0; top: 215px; width: 100%; height: 8px;
    background: var(--sky);
  }
  .card-back .panel {
    position: absolute; left: 0; top: 223px; width: 100%; bottom: 0;
    background: var(--royal);
    display: flex; flex-direction: column; align-items: center;
    padding-top: 18px; color: var(--white);
  }
  .person-name { font-weight: 800; font-size: 25px; letter-spacing: 0.5px; text-transform: uppercase; }
  .person-role { color: var(--sky); font-size: 16px; font-weight: 600; margin-top: -2px; }
  .contact-icons { display: flex; gap: 8px; margin: 8px 0 6px; }
  .contact-icons svg { width: 14px; height: 14px; }
  .contact-list { list-style: none; text-align: center; font-size: 17px; font-weight: 600; line-height: 1.35; }
</style>
</head>
<body>
<main class="canvas">
  <section class="card card-front" aria-label="Card front">
    <div class="brand">
      <span class="brand-mark"></span>
      <span class="brand-name">PKR Tidy Homes<br>Limited</span>
    </div>
    <div class="services">
      <p>SERVICES:</p>
      <p>End of Tenancy</p>
      <p>Carpet &amp; Upholstery</p>
      <p>Regular &amp; One Off</p>
    </div>
  </section>

  <section class="card card-back" aria-label="Card back">
    <div class="top">
      <span class="back-mark"></span>
      <span class="back-name">PKR Tidy Homes</span>
    </div>
    <div class="stripe"></div>
    <div class="panel">
      <p class="person-name">Helen Ashby</p>
      <p class="person-role">Director</p>
      <div class="contact-icons" aria-hidden="true">
        <svg viewBox="0 0 16 16"><path d="M4 1.5 6 4 4.8 5.6a9 9 0 0 0 5.6 5.6L12 10l2.5 2-1.3 2.2C7.5 14 2 8.5 1.8 2.8Z" fill="none" stroke="#29a3df" stroke-width="1.4"/></svg>
        <svg viewBox="0 0 16 16"><rect x="4.5" y="1.5" width="7" height="13" rx="1.5" fill="none" stroke="#29a3df" stroke-width="1.4"/><circle cx="8" cy="12" r="0.9" fill="#29a3df"/></svg>
        <svg viewBox="0 0 16 16"><rect x="1.5" y="3.5" width="13" height="9" rx="1" fill="none" stroke="#29a3df" stroke-width="1.4"/><path d="M1.5 4 8 9l6.5-5" fill="none" stroke="#29a3df" stroke-width="1.4"/></svg>
        <svg viewBox="0 0 16 16"><circle cx="8" cy="8" r="6.5" fill="none" stroke="#29a3df" stroke-width="1.4"/><ellipse cx="8" cy="8" rx="2.8" ry="6.5" fill="none" stroke="#29a3df" stroke-width="1.2"/><path d="M1.5 8h13" stroke="#29a3df" stroke-width="1.2"/></svg>
      </div>
      <ul class="contact-list">
        <li>0800 529 6081</li>
        <li>07438 915 702</li>
        <li>pkrtidy@mailbox-demo.co.uk</li>
        <li>www.pkrtidyhomes.co.uk</li>
      </ul>
    </div>
  </section>
</main>
</body>
</html>
```